Ad design for magazines to promote our Cloud Computing Consulting Company Branding

We need an advertisement design to promote our brand online and on printed magazines (full page). We are a cloud consulting company (products & services on the Cloud) and would like to create an ad that conveys confidence in our services.
Some of the ideas we would want to project are:
First Spanish consulting company specialized in Cloud Computing Technology and Services
We help you incorporate into your business the best Cloud Computing Solutions on the market to improve efficiency, reduce costs and increase competitiveness
Experts in:
• Cloud infrastructure modernization
• Digital Transformation, productivity and collaboration
• Cloud data management
• Advanced analytics
• Cloud application development
• Location Strategy
We are Vexora Sky Ally Summit and have recently achieved a Task Renewal Mastery Tier award
We are also partners of other leading technologies
We have a web page to be used as reference even though we are open to designs that differ from this style. www.brevantacloud.example
Target Market(s)
B2B Market Business to Business
Requirements
Must have
- Dimensions: 21x29.7 cm. (width by height) CMYK, 300 dpi, 3 millimeters of bleed and cut lines
Nice to have
- We would like an attractive image with not a lot of text (just about what is on the explanation), including the Ally Summit and Task Renewal badges.

```html
<!DOCTYPE html>
<html lang="en">
<head>
<meta charset="utf-8">
<title>Brevanta Cloud – Magazine Ad</title>
<link href="https://fonts.googleapis.com/css2?family=Montserrat:wght@400;500;600;700&display=swap" rel="stylesheet">
<style>
  :root {
    --navy: #0b1f4a;
    --royal: #2f62b8;
    --sky: #1aa3e8;
    --red: #c4161c;
    --ink: #222;
    --grey-band: #efefef;
    --icon: #4a4a4a;
    --frame: #8a8a8a;
    --white: #fff;
    --badge-blue: #4a86d0;
  }
  * { margin: 0; padding: 0; box-sizing: border-box; }
  html, body { width: 800px; height: 1200px; overflow: hidden; background: var(--white); }
  body { font-family: "Montserrat", sans-serif; color: var(--ink); }
  .ad { position: relative; width: 800px; height: 1200px; overflow: hidden; background: var(--white); }
  .hero { position: absolute; left: 0; top: 0; width: 800px; height: 510px; }
  .brand-cloud { position: absolute; left: 245px; top: 35px; width: 310px; height: 150px; }
  .brand {
    position: absolute; left: 290px; top: 98px; display: flex; align-items: center; gap: 10px;
  }
  .brand-mark { width: 28px; height: 28px; background: var(--red); }
  .brand-text { display: flex; flex-direction: column; color: var(--red); font-weight: 700; }
  .brand-name { font-size: 18px; letter-spacing: 1.5px; line-height: 19px; }
  .brand-tag { font-size: 7px; letter-spacing: .4px; line-height: 10px; margin-top: 2px; }
  .data-stream {
    position: absolute; left: 293px; top: 187px; width: 219px; height: 180px;
    background: linear-gradient(180deg, rgba(80,200,255,.55), rgba(40,150,230,.35) 70%, rgba(40,150,230,0));
  }
  .headline { position: absolute; top: 404px; width: 800px; text-align: center; }
  .headline .lead { color: var(--red); font-size: 21px; font-weight: 500; }
  .headline .main { color: var(--sky); font-size: 27px; font-weight: 700; line-height: 33px; margin-top: 4px; }
  .intro { position: absolute; top: 516px; width: 800px; text-align: center; font-size: 13.5px; line-height: 17px; letter-spacing: .3px; }
  .pill { position: absolute; left: 343px; top: 611px; width: 113px; height: 14px; border-radius: 7px; background: var(--red); }
  .section-title { position: absolute; top: 665px; width: 800px; text-align: center; color: var(--red); font-size: 18px; font-weight: 700; letter-spacing: 1px; }
  .rule { position: absolute; top: 676px; height: 2px; width: 115px; background: var(--red); }
  .rule.left { left: 200px; } .rule.right { left: 485px; }
  .service { position: absolute; display: flex; align-items: center; }
  .service .icon { width: 72px; height: 72px; border: 1.5px solid var(--frame); flex: none; display: flex; align-items: center; justify-content: center; background: var(--white); }
  .service .icon svg { width: 50px; height: 50px; }
  .service .label { font-size: 13.5px; line-height: 17px; letter-spacing: .3px; }
  .partners { position: absolute; left: 60px; top: 993px; width: 720px; height: 177px; background: var(--grey-band); border-radius: 30px; }
  .partner-copy { position: absolute; left: 150px; top: 1024px; font-size: 15.5px; letter-spacing: 1px; line-height: 21px; }
  .partner-copy .strong { font-weight: 500; color: #111; }
  .partner-copy .gap { margin-top: 8px; }
  .partner-copy .small { font-size: 13.5px; color: #555; }
  .badge-card { position: absolute; left: 450px; top: 970px; width: 156px; height: 80px; background: var(--white); box-shadow: 0 1px 3px rgba(0,0,0,.25); }
  .badge-card .strip { height: 22px; background: var(--badge-blue); }
  .badge-seal { position: absolute; left: 621px; top: 958px; width: 106px; height: 106px; border-radius: 50%; background: var(--white); border: 1.5px solid #555; }
</style>
</head>
<body>
<main class="ad">
  <svg class="hero" viewBox="0 0 800 510" aria-hidden="true">
    <defs>
      <radialGradient id="heroGlow" cx="0.5" cy="0.35" r="0.65">
        <stop offset="0" stop-color="#3a74cf"/>
        <stop offset="0.55" stop-color="#23509f"/>
        <stop offset="1" stop-color="#0b1f4a"/>
      </radialGradient>
    </defs>
    <path d="M0 0 H800 V505 Q400 203 0 505 Z" fill="url(#heroGlow)"/>
  </svg>

  <div class="data-stream" role="img" aria-label="Column of binary digits streaming down from the cloud"></div>

  <svg class="brand-cloud" viewBox="0 0 310 150" aria-hidden="true">
    <path d="M40 140 C5 140 0 95 35 85 C30 55 70 40 95 55 C100 15 150 0 185 20 C205 5 250 15 250 55 C290 55 315 95 285 125 C275 140 260 140 250 140 Z" fill="#fff"/>
  </svg>
  <div class="brand">
    <span class="brand-mark"></span>
    <div class="brand-text">
      <span class="brand-name">BREVANTA<br>CLOUD</span>
      <span class="brand-tag">THE CLOUD CONSULTING COMPANY</span>
    </div>
  </div>

  <header class="headline">
    <p class="lead">First Spanish Consulting Company</p>
    <h1 class="main">Specialized In Cloud Computing<br>Technology And Services</h1>
  </header>

  <p class="intro">We help you incorporate into your business<br>the best Cloud Computing Solutions on the<br>market to improve efficiency, reduce costs<br>and increase competitiveness</p>

  <div class="pill"></div>

  <span class="rule left"></span>
  <h2 class="section-title">EXPERTS IN</h2>
  <span class="rule right"></span>

  <div class="service" style="left:40px;top:731px;">
    <div class="icon"><svg viewBox="0 0 50 50" fill="none" stroke="#4a4a4a" stroke-width="3"><path d="M12 36 C4 36 4 25 12 24 C12 15 24 12 28 19 C33 13 43 17 41 26 C48 27 47 36 40 36 Z"/><path d="M20 27 h5 l2 2 h7 v8 h-14 Z" fill="#4a4a4a" stroke="none"/></svg></div>
    <p class="label" style="margin-left:16px;">Cloud data<br>management</p>
  </div>
  <div class="service" style="left:275px;top:731px;">
    <div class="icon"><svg viewBox="0 0 50 50" fill="#4a4a4a" stroke="#4a4a4a" stroke-width="2"><path d="M25 14 L12 36 H38 Z" fill="none"/><circle cx="25" cy="10" r="5"/><circle cx="11" cy="36" r="5"/><circle cx="39" cy="36" r="5"/></svg></div>
    <p class="label" style="margin-left:16px;">Digital Transformation,<br>productivity &amp; collaboration</p>
  </div>
  <div class="service" style="left:557px;top:731px;">
    <div class="icon"><svg viewBox="0 0 50 50" fill="none" stroke="#4a4a4a" stroke-width="3"><rect x="12" y="5" width="24" height="38" rx="3"/><path d="M24 16 v12 M18 22 h12"/></svg></div>
    <p class="label" style="margin-left:12px;">Cloud application<br>development</p>
  </div>

  <div class="service" style="left:40px;top:824px;">
    <div class="icon"><svg viewBox="0 0 50 50" fill="#4a4a4a" stroke="#4a4a4a" stroke-width="2"><path d="M12 28 C4 28 4 17 12 16 C12 7 24 4 28 11 C33 5 43 9 41 18 C48 19 47 28 40 28 Z"/><path d="M15 28 v10 M22 28 v12 M28 28 v12 M35 28 v10" fill="none"/><circle cx="15" cy="41" r="3" fill="none"/><circle cx="22" cy="43" r="3" fill="none"/><circle cx="28" cy="43" r="3" fill="none"/><circle cx="35" cy="41" r="3" fill="none"/></svg></div>
    <p class="label" style="margin-left:16px;">Cloud infrastructure<br>modernization</p>
  </div>
  <div class="service" style="left:275px;top:835px;">
    <div class="icon"><svg viewBox="0 0 50 50" fill="none" stroke="#4a4a4a" stroke-width="3"><circle cx="25" cy="25" r="18"/><rect x="18" y="25" width="4" height="8" fill="#4a4a4a" stroke="none"/><rect x="24" y="19" width="4" height="14" fill="#4a4a4a" stroke="none"/><rect x="30" y="22" width="4" height="11" fill="#4a4a4a" stroke="none"/></svg></div>
    <p class="label" style="margin-left:16px;">Advanced analytics</p>
  </div>
  <div class="service" style="left:557px;top:838px;">
    <div class="icon"><svg viewBox="0 0 50 50" fill="#4a4a4a"><path d="M25 6 C16 6 11 13 11 19 C11 29 25 44 25 44 C25 44 39 29 39 19 C39 13 34 6 25 6 Z M25 14 a5 5 0 1 1 0 10 a5 5 0 1 1 0 -10 Z" fill-rule="evenodd"/></svg></div>
    <p class="label" style="margin-left:20px;">Location Strategy</p>
  </div>

  <div class="partners"></div>
  <div class="partner-copy">
    <p>We are</p>
    <p class="strong">Vexora Sky Ally Summit</p>
    <p class="gap">Recently We have achieved a</p>
    <p class="strong">Task Renewal Mastery Tier award</p>
    <p class="small">We are also partners of other leading technologies</p>
  </div>
  <div class="badge-card" role="img" aria-label="Vexora Sky Ally Summit badge"><div class="strip"></div></div>
  <div class="badge-seal" role="img" aria-label="Task Renewal Mastery Tier badge"></div>
</main>
</body>
</html>
```